Wine Label Design

Organization name: Orvell Wine Company

My company is called Orvell Wine Company, I’m a wine importer and wholesaler who distributes wine domestically.

We are about to launch a line of three premium and one sparkling wine that we will wholesale to various retailers, wine stores, and restaurants for re-sale. The wines label will have “Dean Marlowe” I plan on having the labels the same and just changing the varietal as needed. My wine are made from premium grapes and will be marketed as a high end wine. My current label size is 3 1/2" wide by 5" in long and the labels can be on a solid background or transparent.

I would like the first label to be for my Cabernet Sauvignon, California, 2012, 750ML (for the size of the bottle) and ALC 13.8% BY VOL (for the alcohol content).

Colors: I am open to any and all designs that would alter my perception of what will be best!

Further:
Current label is boring and poorly done, so hopefully you designers can come up with something better

Industry/Entity Type

It Company

```html
<!DOCTYPE html>
<html lang="en">
<head>
<meta charset="UTF-8">
<title>Dean Marlowe Cabernet Sauvignon Label</title>
<link href="https://fonts.googleapis.com/css2?family=Kalam:wght@400&family=Petit+Formal+Script&family=Tinos:ital@0;1&display=swap" rel="stylesheet">
<style>
  :root {
    --canvas: #ffffff;
    --label-black: #000000;
    --band-light: #676767;
    --band-mid: #5c5c5c;
    --art-dark: #1c1c1c;
    --art-grey: #6e6e6e;
    --ink-light: #d6d6d6;
    --ink-soft: #b9b9b9;
    --ink-white: #ffffff;
    --shadow: #3a3a3a;
  }
  html, body {
    margin: 0;
    padding: 0;
    width: 1200px;
    height: 1000px;
    overflow: hidden;
    background: var(--canvas);
  }
  .canvas {
    position: relative;
    width: 1200px;
    height: 1000px;
  }
  .label {
    position: absolute;
    left: 278px;
    top: 18px;
    width: 644px;
    height: 944px;
    background: var(--label-black);
    box-shadow: 10px 10px 6px var(--shadow);
  }
  .side-band {
    position: absolute;
    left: 490px;
    top: 12px;
    width: 142px;
    height: 753px;
    background: var(--band-light);
  }
  .region-band {
    position: absolute;
    left: 57px;
    top: 650px;
    width: 575px;
    height: 115px;
    background: var(--band-mid);
  }
  .label-art {
    position: absolute;
    left: 57px;
    top: 12px;
    width: 433px;
    height: 638px;
    background:
      linear-gradient(160deg, transparent 38%, rgba(110,110,110,0.55) 48%, transparent 58%),
      linear-gradient(115deg, var(--art-dark) 0%, #2e2e2e 35%, var(--art-grey) 55%, #2a2a2a 75%, var(--art-dark) 100%);
  }
  .tagline {
    position: absolute;
    left: 18px;
    top: 760px;
    width: 750px;
    transform: rotate(-90deg);
    transform-origin: 0 0;
    font-family: "Tinos", serif;
    font-style: italic;
    font-size: 31px;
    color: var(--band-light);
    white-space: nowrap;
    letter-spacing: 0.5px;
  }
  .brand-name {
    position: absolute;
    left: 70px;
    top: 112px;
    margin: 0;
    font-family: "Kalam", cursive;
    font-weight: 400;
    font-size: 78px;
    line-height: 1;
    color: var(--ink-light);
    letter-spacing: 1px;
  }
  .region {
    position: absolute;
    left: 72px;
    top: 688px;
    font-family: "Kalam", cursive;
    font-size: 50px;
    line-height: 1;
    color: var(--ink-white);
    text-shadow: 2px 2px 2px #000;
  }
  .vintage {
    position: absolute;
    right: 22px;
    top: 672px;
    font-family: "Tinos", serif;
    font-size: 34px;
    line-height: 38px;
    color: var(--ink-light);
    text-align: right;
    letter-spacing: 1px;
  }
  .varietal {
    position: absolute;
    left: 0;
    width: 644px;
    top: 818px;
    text-align: center;
    font-family: "Petit Formal Script", cursive;
    font-size: 44px;
    line-height: 1;
    color: var(--ink-soft);
    word-spacing: 14px;
  }
  .volume, .alcohol {
    position: absolute;
    top: 920px;
    font-family: "Tinos", serif;
    font-size: 20px;
    line-height: 1;
    color: var(--ink-white);
  }
  .volume { left: 10px; }
  .alcohol { right: 10px; }
</style>
</head>
<body>
<div class="canvas">
  <section class="label">
    <div class="side-band"></div>
    <div class="region-band"></div>
    <div class="label-art" role="img" aria-label="Abstract grey splash artwork of poured wine on a dark background"></div>
    <div class="tagline">wine made from premium grapes</div>
    <h1 class="brand-name">Dean Marlowe</h1>
    <div class="region">CALIFORNIA</div>
    <div class="vintage">Vintage<br>2012</div>
    <div class="varietal">Cabernet Sauvignon</div>
    <div class="volume">750ML</div>
    <div class="alcohol">ALC 13,8%</div>
  </section>
</div>
</body>
</html>
```